Business Card Design Project

We're an orthopaedic office, and our colors are blue white and balck. Dealing with physicians and healthcare execs, I'd like this card to have a classy, yet overpowering wow factor.

Here are a couple of cards I like that are close to what I'm looking for:
http://www.pixelbazaro.com/design/392047
http://www.pixelbazaro.com/design/286390

Industry/Entity Type

Healthcare

```html
<!DOCTYPE html>
<html lang="en">
<head>
<meta charset="utf-8">
<title>Pine Ridge Business Card</title>
<link href="https://fonts.googleapis.com/css2?family=Jost:ital,wght@0,400;0,500;1,400;1,600&display=swap" rel="stylesheet">
<style>
  :root {
    --page: #ecebe8;
    --card-blue: #2534a0;
    --card-blue-deep: #1d2a88;
    --ink-light: #eef0f6;
    --ink-soft: #d9dcea;
    --shadow: rgba(20, 20, 40, 0.28);
  }
  * { margin: 0; padding: 0; box-sizing: border-box; }
  html, body {
    width: 1200px; height: 880px; overflow: hidden;
    background: var(--page);
    font-family: "Jost", "Futura", sans-serif;
  }
  .stage { position: relative; width: 1200px; height: 880px; }
  .card {
    position: absolute; left: 320px; width: 560px; height: 320px;
    background: linear-gradient(135deg, var(--card-blue) 0%, var(--card-blue-deep) 100%);
    box-shadow: 0 10px 24px var(--shadow);
    color: var(--ink-light);
    overflow: hidden;
  }
  .card--front { top: 95px; }
  .card--back { top: 465px; }

  /* Front */
  .front-mark {
    position: absolute; left: 34px; top: 40px;
    width: 240px; height: 240px; border-radius: 50%;
    background: var(--ink-soft);
  }
  .front-name {
    position: absolute; right: 34px; bottom: 52px; text-align: right;
  }
  .brand-title {
    font-weight: 400; letter-spacing: 1px; line-height: 1;
    font-size: 40px; color: var(--ink-light);
  }
  .brand-sub {
    font-weight: 400; font-size: 17px; line-height: 1.15;
    color: var(--ink-light); margin-top: 4px;
  }

  /* Back */
  .back-brand {
    position: absolute; right: 36px; top: 46px; text-align: right;
    display: flex; align-items: flex-start; gap: 14px;
  }
  .back-brand .mini-mark {
    width: 58px; height: 58px; border-radius: 50%;
    background: var(--ink-soft); flex: none;
  }
  .back-brand .brand-title { font-size: 28px; }
  .back-brand .brand-sub { font-size: 13px; }

  .holder {
    position: absolute; left: 36px; top: 150px;
  }
  .holder-name { font-weight: 600; font-style: italic; font-size: 20px; }
  .holder-role { font-style: italic; font-size: 13px; color: var(--ink-soft); }

  .contact {
    position: absolute; left: 250px; top: 160px;
    list-style: none; font-size: 16px; line-height: 1.45; color: var(--ink-light);
  }
</style>
</head>
<body>
<main class="stage">
  <section class="card card--front" aria-label="Card front">
    <div class="front-mark"></div>
    <div class="front-name">
      <div class="brand-title">PINE RIDGE</div>
      <div class="brand-sub">Orthopaedic &amp; Sports<br>Medicine Center</div>
    </div>
  </section>

  <section class="card card--back" aria-label="Card back">
    <div class="back-brand">
      <div class="mini-mark"></div>
      <div>
        <div class="brand-title">PINE RIDGE</div>
        <div class="brand-sub">Orthopaedic &amp; Sports<br>Medicine Center</div>
      </div>
    </div>
    <div class="holder">
      <div class="holder-name">Daniel Hartley</div>
      <div class="holder-role">CEO</div>
    </div>
    <ul class="contact">
      <li>(555) 014-2760</li>
      <li>dhartley@pineridgeortho.com</li>
      <li>1820 Cedar Hollow Rd., Fairview, LA 70000</li>
    </ul>
  </section>
</main>
</body>
</html>
```